Homepage web design

I need a homepage design that will be easy to build into a default Word Press theme. Basically, header, navigation, body with sidebar, and footer.

This website is for a small commercial real estate firm in the Washington DC, Maryland and Virginia market.

THIS IS NOT A HOUSING/RESIDENTIAL WEBSITE. PLEASE DO NOT ADD ANY PROPERTY SEARCH FUNCTIONALITY.

Target Market(s)

People looking for basic information about the team and services provided.

Industry/Entity Type

Real Estate

Requirements
Must have
• Professional look. Clean design.

```html
<!DOCTYPE html>
<html lang="en">
<head>
<meta charset="utf-8">
<title>Meridian Commercial Realty — Home</title>
<link rel="stylesheet" href="https://fonts.googleapis.com/css2?family=Lato:wght@300;400;700&family=Arimo:ital,wght@0,400;0,700;1,400&family=Oswald:wght@500&family=Playfair+Display:wght@700&display=swap">
<style>
:root{
  --green:#0e8653;
  --green-text:#17885a;
  --ink:#1d1d1d;
  --body:#333;
  --page:#f1f1f1;
  --card:#ffffff;
  --line:#e3e3e3;
  --nav-top:#4a4a4a;
  --nav-bottom:#2a2a2a;
  --footer:#0d0d0d;
  --footer-text:#9a9a9a;
}
*{box-sizing:border-box;margin:0;padding:0}
html,body{width:1200px;height:2438px;overflow:hidden}
body{position:relative;background:var(--page);font-family:"Arimo",Arial,sans-serif;color:var(--body)}
.abs{position:absolute}

/* header */
.site-header{left:0;top:0;width:1200px;height:133px;background:linear-gradient(#ffffff,#ececec)}
.brand{left:133px;top:52px;display:flex;align-items:center;gap:10px}
.brand-mark{width:22px;height:22px;background:var(--green)}
.brand-name{font-family:"Lato",sans-serif;font-weight:700;font-size:30px;color:var(--green);letter-spacing:1px}
.call{left:830px;top:34px;font-family:"Lato",sans-serif;width:160px}
.call-label{font-size:23px;color:#222;font-weight:400;white-space:nowrap}
.call-number{font-size:21px;color:var(--green);font-weight:700;white-space:nowrap}
.agent-photo{left:998px;top:8px;width:72px;height:125px;border-radius:36px 36px 0 0;background:linear-gradient(#e8e2dc,#f5f5f5)}

/* navigation */
.main-nav{left:0;top:133px;width:1200px;height:47px;background:linear-gradient(var(--nav-top),var(--nav-bottom))}
.nav-item{position:absolute;top:0;height:47px;line-height:47px;font-size:14px;color:#fff;text-transform:uppercase}
.nav-item.active{background:var(--green);width:89px;text-align:center}
.search{left:832px;top:10px;width:235px;height:27px;display:flex}
.search-field{flex:1;background:#fff;border:1px solid #ccc}
.search-btn{width:34px;background:var(--green);display:flex;align-items:center;justify-content:center}

/* hero */
.hero{left:0;top:180px;width:1200px;height:495px;background:linear-gradient(180deg,#3f5a2e 0%,#7b7f72 35%,#c9c7bf 60%,#566b33 85%,#3e5a1f 100%)}
.hero-arrow{top:390px}
.hero-title{left:517px;top:480px;width:543px;height:57px;background:var(--green);opacity:.92;font-family:"Oswald",sans-serif;font-size:46px;line-height:57px;color:#fff;text-align:center;letter-spacing:1px}
.hero-sub{left:517px;top:538px;width:455px;height:35px;background:rgba(20,20,20,.8);font-family:"Oswald",sans-serif;font-size:23px;line-height:35px;color:#fff;padding-left:12px}

/* welcome */
.welcome{left:133px;top:722px;width:630px}
.welcome h1{font-family:"Lato",sans-serif;font-weight:300;font-size:33px;letter-spacing:-.3px;white-space:nowrap;color:var(--ink);margin-bottom:22px}
.welcome h1 span{color:var(--green-text)}
.welcome p{font-size:12.5px;line-height:17px;color:#222;margin-bottom:17px}
.welcome .note{font-style:italic;color:var(--green-text);font-size:11.5px}

/* featured */
.featured{left:133px;top:1007px;width:630px;height:1001px;background:var(--card);border:1px solid var(--line)}
.featured h2{position:absolute;left:18px;top:14px;font-family:"Lato",sans-serif;font-weight:300;font-size:33px;color:var(--green-text)}
.featured .rule{position:absolute;left:12px;right:12px;top:64px;border-top:2px solid #eee}
.property{position:absolute;left:20px;width:590px}
.property-photo{width:590px;height:213px}
.property h3{font-family:"Lato",sans-serif;font-weight:400;font-size:19px;color:#111;margin:12px 0 8px}
.property p{font-size:12.5px;line-height:17.5px;color:#333}
.read-more{float:right;color:var(--green-text);font-style:italic;font-size:11.5px}
.specs{display:flex;align-items:center;margin-top:18px}
.spec{display:flex;align-items:flex-start;gap:6px;width:105px}
.spec-icon{width:26px;height:26px;border-radius:50%;background:var(--green);display:flex;align-items:center;justify-content:center;margin-top:3px}
.spec-num{font-family:"Lato",sans-serif;font-size:20px;line-height:20px;color:#111}
.spec-label{font-size:11.5px;color:#333}
.price{margin-left:8px;width:112px;height:33px;border-radius:17px;background:#111;color:#fff;font-family:"Lato",sans-serif;font-weight:700;font-size:18px;line-height:33px;text-align:center}
.sold{position:absolute;right:0;top:0;width:70px;height:70px;overflow:hidden}
.sold span{position:absolute;right:-26px;top:16px;width:110px;height:18px;background:var(--green);color:#fff;font-size:10px;font-weight:700;text-align:center;line-height:18px;transform:rotate(45deg)}
.divider-dashed{position:absolute;left:12px;right:12px;top:489px;border-top:1px dashed #ccc}
.divider-solid{position:absolute;left:12px;right:12px;top:934px;border-top:2px solid #eee}
.pager{position:absolute;left:453px;top:960px;display:flex}
.pager span{width:30px;height:30px;line-height:30px;text-align:center;font-size:14px;color:#444}
.pager .current{background:#eee;border:1px solid #ccc}

/* sidebar */
.side-box{left:820px;width:247px;background:var(--card);border:1px solid var(--line)}
.side-head{background:var(--green);color:#fff;font-family:"Lato",sans-serif;font-weight:400;font-size:25px;height:50px;line-height:50px;padding-left:18px}
.about-box{top:730px;height:470px}
.about-box p{font-size:11.5px;line-height:17px;color:#444;padding:0 18px;margin-top:20px}
.about-box .read-more{float:none;display:block;padding:0 18px;margin-top:18px}
.recent-box{top:1233px;height:467px}
.recent-box h2{font-family:"Lato",sans-serif;font-weight:300;font-size:25px;color:var(--green-text);padding:18px 0 0 18px}
.recent-box .rule{margin:12px 12px 0;border-top:2px solid #eee}
.post{display:flex;gap:7px;padding:18px 6px 0 14px;height:100px;border-bottom:1px dashed #ddd;margin-right:12px}
.post:last-child{border-bottom:none}
.post-thumb{width:58px;height:58px;flex:none;border:1px solid #ddd;background:linear-gradient(#d9d4cf,#b8aea4)}
.post-text{font-size:11px;line-height:15.5px;color:#333}
.post-date{display:block;color:var(--green-text);font-style:italic;font-size:11px}
.promo{left:820px;top:1730px;width:247px;height:278px;background:linear-gradient(#1b63b8 0%,#7fb3e3 50%,#c8dbe6 72%,#4d6f36 100%);text-align:center}
.promo-title{margin-top:30px;font-family:"Playfair Display",serif;font-weight:700;font-size:35px;line-height:36px;color:#fff}
.promo-btn{position:absolute;left:55px;top:237px;width:137px;height:33px;background:#111;color:#fff;font-weight:700;font-size:18px;line-height:33px}

/* footer */
.site-footer{left:0;top:2070px;width:1200px;height:368px;background:var(--footer)}
.foot-col{top:2103px}
.foot-col h4{font-weight:700;font-size:16px;color:var(--green);margin-bottom:14px}
.foot-col ul{list-style:none}
.foot-col li{font-size:13.5px;color:var(--footer-text);height:32px;display:flex;align-items:center;gap:6px}
.foot-col li::before{content:"";width:7px;height:7px;border-radius:50%;background:var(--green)}
.foot-contact p{font-size:13.5px;line-height:18px;color:var(--footer-text);width:225px}
.foot-contact .contact-line{color:#eee;margin-top:10px;white-space:nowrap}
.foot-contact .contact-line+.contact-line{margin-top:0}
.socials{display:flex;gap:9px;margin-top:14px}
.socials span{width:32px;height:32px;border-radius:50%;background:var(--green)}
.map{left:810px;top:2112px;width:245px;height:191px;background:linear-gradient(135deg,#eceae3,#dcdccf)}
.foot-rule{left:138px;top:2342px;width:925px;border-top:1px solid #2a2a2a}
.foot-nav{left:0;top:2364px;width:1200px;text-align:center;font-size:13.5px;color:var(--footer-text)}
.foot-nav a{color:var(--footer-text);text-decoration:none;padding:0 11px}
.foot-nav a.current{color:#fff}
.foot-nav i{color:#555;font-style:normal}
.copyright{left:0;top:2399px;width:1200px;text-align:center;font-size:11.5px;color:#888}
</style>
</head>
<body>

<header class="site-header abs">
  <div class="brand abs"><span class="brand-mark"></span><span class="brand-name">MCR</span></div>
  <div class="call abs">
    <div class="call-label">Call Us Now:</div>
    <div class="call-number">000-00000000</div>
  </div>
  <div class="agent-photo abs" role="img" aria-label="Photo of a customer service agent wearing a headset"></div>
</header>

<nav class="main-nav abs">
  <span class="nav-item active" style="left:133px">Home</span>
  <span class="nav-item" style="left:242px">About Us</span>
  <span class="nav-item" style="left:350px">Find a Home</span>
  <span class="nav-item" style="left:480px">Blog</span>
  <span class="nav-item" style="left:560px">Services</span>
  <span class="nav-item" style="left:663px">Contact Us</span>
  <div class="search abs">
    <span class="search-field"></span>
    <span class="search-btn"><svg width="16" height="16" viewBox="0 0 16 16"><circle cx="6.5" cy="6.5" r="4.5" fill="none" stroke="#fff" stroke-width="2"/><line x1="10" y1="10" x2="14.5" y2="14.5" stroke="#fff" stroke-width="2.4"/></svg></span>
  </div>
</nav>

<section class="hero abs" role="img" aria-label="Photo of a large building surrounded by trees and lawn"></section>
<svg class="hero-arrow abs" style="left:30px" width="34" height="54" viewBox="0 0 34 54"><polyline points="28,4 6,27 28,50" fill="none" stroke="#fff" stroke-width="6"/></svg>
<svg class="hero-arrow abs" style="left:1136px" width="34" height="54" viewBox="0 0 34 54"><polyline points="6,4 28,27 6,50" fill="none" stroke="#fff" stroke-width="6"/></svg>
<div class="hero-title abs">LOREM IPSUM DOLOR</div>
<div class="hero-sub abs">CONSECTETUR ADIPISCING ELIT. NULLA LOBORTIS</div>

<section class="welcome abs">
  <h1>Welcome to <span>Meridian Commercial Realty</span></h1>
  <p>Lorem ipsum dolor sit amet, consectetur adipiscing elit. Nulla lobortis consequat mauris, eget eleifend nunc viverra viverra. Ut ac risus odio. Aliquam pretium purus sed nulla feugiat blandit. Cras vel libero ut lacus</p>
  <p>Eleifend tempor. Phasellus eleifend, magna non tincidunt accumsan, justo arcu cursus ipsum, non porttitor sapien quam vel magna. Maecenas elit nisl, molestie nec dapibus nec, aliquet a erat. Donec scelerisque lacus a libero suscipit auctor volutpat enim euismod. Mauris porta, lacus ut ullamcorper sodales, mauris tortor feugiat purus, nec aliquam neque purus ac metus. Nunc eleifend leo quis nisl hendrerit ultrices. Suspendisse quis feugiat elit. Fusce vitae dolor ac est tincidunt feugiat. Phasellus volutpat dui in sapien malesuada tempus placerat justo ultricies. Duis mollis ornare risus, ut consectetur mi tincidunt sit amet. Maecenas quis nibh</p>
  <p class="note">Donec a lectus non purus ultricies eleifend.</p>
</section>

<section class="featured abs">
  <h2>Featured Property</h2>
  <div class="rule"></div>

  <article class="property" style="top:92px">
    <div class="property-photo" role="img" aria-label="Photo of a stone and siding office building" style="background:linear-gradient(#7f8c6a,#9a8a78 45%,#6d7f4a)"></div>
    <h3>Lorem ipsum dolor sit amet, consectetur adipiscing elit</h3>
    <p>Lorem ipsum dolor sit amet, consectetur adipiscing elit. Nulla lobortis consequat mauris, eget eleifend nunc viverra viverra. Ut ac risus odio. Aliquam pretium purus sed nulla feugiat blandit. Cras vel libero ut lacus Eleifend tempor. Phasellus eleifend, magna non <span class="read-more">[ Read more ]</span></p>
    <div class="specs">
      <div class="spec"><span class="spec-icon"><svg width="14" height="12" viewBox="0 0 14 12"><rect x="0" y="0" width="14" height="3" fill="#fff"/><rect x="0" y="4.5" width="14" height="3" fill="#fff"/><rect x="0" y="9" width="14" height="3" fill="#fff"/></svg></span><div><div class="spec-num">3</div><div class="spec-label">Floors</div></div></div>
      <div class="spec"><span class="spec-icon"><svg width="12" height="14" viewBox="0 0 12 14"><path d="M1 0h10v14H1z" fill="#fff"/><circle cx="8.5" cy="7.5" r="1.2" fill="#0e8653"/></svg></span><div><div class="spec-num">2</div><div class="spec-label">Suites</div></div></div>
      <div class="spec"><span class="spec-icon"><svg width="14" height="10" viewBox="0 0 14 10"><path d="M2 4l2-4h6l2 4h2v4H0V4z" fill="#fff"/><circle cx="3.5" cy="8.5" r="1.5" fill="#fff"/><circle cx="10.5" cy="8.5" r="1.5" fill="#fff"/></svg></span><div><div class="spec-num">1</div><div class="spec-label">Parking</div></div></div>
      <div class="price">$000.00</div>
    </div>
  </article>

  <div class="divider-dashed"></div>

  <article class="property" style="top:511px">
    <div class="property-photo" role="img" aria-label="Photo of a white building with a glass front under a blue sky" style="background:linear-gradient(#5d8fd0,#a9c7e8 40%,#8a8f86 65%,#4f7a34)"></div>
    <div class="sold"><span>SOLD</span></div>
    <h3>Lorem ipsum dolor sit amet, consectetur adipiscing elit</h3>
    <p>Lorem ipsum dolor sit amet, consectetur adipiscing elit. Nulla lobortis consequat mauris, eget eleifend nunc viverra viverra. Ut ac risus odio. Aliquam pretium purus sed nulla feugiat blandit. Cras vel libero ut lacus Eleifend tempor. Phasellus eleifend, magna non <span class="read-more">[ Read more ]</span></p>
    <div class="specs">
      <div class="spec"><span class="spec-icon"><svg width="14" height="12" viewBox="0 0 14 12"><rect x="0" y="0" width="14" height="3" fill="#fff"/><rect x="0" y="4.5" width="14" height="3" fill="#fff"/><rect x="0" y="9" width="14" height="3" fill="#fff"/></svg></span><div><div class="spec-num">3</div><div class="spec-label">Floors</div></div></div>
      <div class="spec"><span class="spec-icon"><svg width="12" height="14" viewBox="0 0 12 14"><path d="M1 0h10v14H1z" fill="#fff"/><circle cx="8.5" cy="7.5" r="1.2" fill="#0e8653"/></svg></span><div><div class="spec-num">2</div><div class="spec-label">Suites</div></div></div>
      <div class="spec"><span class="spec-icon"><svg width="14" height="10" viewBox="0 0 14 10"><path d="M2 4l2-4h6l2 4h2v4H0V4z" fill="#fff"/><circle cx="3.5" cy="8.5" r="1.5" fill="#fff"/><circle cx="10.5" cy="8.5" r="1.5" fill="#fff"/></svg></span><div><div class="spec-num">1</div><div class="spec-label">Parking</div></div></div>
      <div class="price">$000.00</div>
    </div>
  </article>

  <div class="divider-solid"></div>
  <div class="pager"><span class="current">1</span><span>2</span><span>3</span><span>4</span><span>5</span></div>
</section>

<aside class="side-box about-box abs">
  <h2 class="side-head">About Us</h2>
  <p>Lorem ipsum dolor sit amet, consectetur adipiscing elit. Nulla lobortis consequat mauris, eget eleifend nunc viverra</p>
  <p>Viverra. Ut ac risus odio. Aliquam tium purus sed nulla feugiat blandit. Cras vel libero ut lacus eleifend tempor. sellus eleifend, magna non tincidunt umsan, justo arcu cursus ipsum, non porttitor sapien quam vel magna. Maecenas elit nisl, molestie nec dapibus nec, aliquet a erat. Donec scelerisque lacus a libero suscipit auctor volutpat enim euismod. Mauris porta, lacus ut ullamcorper sodales, mauris tortor feugiat purus, nec aliquam neque purus ac metus. Nunc eleifend leo quis nisl hendrerit ultrices. Suspendisse quis feugiat elit. Fusce vitae dolor ac est tincidunt feugiat. Phasellus volutpat dui in sapien</p>
  <span class="read-more">[ Read more ]</span>
</aside>

<aside class="side-box recent-box abs">
  <h2>Recent Post</h2>
  <div class="rule"></div>
  <div class="post"><span class="post-thumb" role="img" aria-label="Author portrait"></span><p class="post-text">Lorem ipsum dolor sit amet, consectetur adipiscing elit. Nulla lobortis consequat<span class="post-date">August 2nd, 2013</span></p></div>
  <div class="post"><span class="post-thumb" role="img" aria-label="Author portrait"></span><p class="post-text">Lorem ipsum dolor sit amet, consectetur adipiscing elit. Nulla lobortis consequat<span class="post-date">August 4th, 2013</span></p></div>
  <div class="post"><span class="post-thumb" role="img" aria-label="Author portrait"></span><p class="post-text">Lorem ipsum dolor sit amet, consectetur adipiscing elit. Nulla lobortis consequat<span class="post-date">August 6th, 2013</span></p></div>
  <div class="post"><span class="post-thumb" role="img" aria-label="Author portrait"></span><p class="post-text">Lorem ipsum dolor sit amet, consectetur adipiscing elit. Nulla lobortis consequat<span class="post-date">August 10th, 2013</span></p></div>
</aside>

<aside class="promo abs" role="img" aria-label="Advertisement showing a white office building under a blue sky">
  <div class="promo-title">Real Estate<br>Real Value</div>
  <div class="promo-btn">Know More</div>
</aside>

<footer class="site-footer abs"></footer>
<div class="foot-col abs" style="left:147px">
  <h4>Aenean dapibus</h4>
  <ul><li>Lorem laoreet ante pharetra</li><li>Ornare malesuada orci</li><li>Ornare. Ut volutpat ipsum</li><li>Ipsum, eget suscipit mauris.</li><li>Sed sed nisl ac justo</li></ul>
</div>
<div class="foot-col abs" style="left:360px">
  <h4>Aliquam quis mauris</h4>
  <ul><li>Sed lacinia vulputate dolor,</li><li>Nec congue nunc</li><li>Accumsan at. Praesent leo</li><li>Magna, imperdiet et mollis</li><li>Sed, hendrerit id nunc.</li></ul>
</div>
<div class="foot-col foot-contact abs" style="left:575px">
  <h4>Contact Information</h4>
  <p>Sed lacinia vulputate dolor, Nec congue nunc Accumsan at. Praesent leo Magna,</p>
  <p class="contact-line">Phone: 000-00000000</p>
  <p class="contact-line">Email: hello@mcrealty.example</p>
  <div class="socials"><span></span><span></span><span></span></div>
</div>
<div class="map abs" role="img" aria-label="Street map showing the office location"></div>
<div class="foot-rule abs"></div>
<nav class="foot-nav abs"><a class="current">Home</a><i>|</i><a>About Us</a><i>|</i><a>Find a Home</a><i>|</i><a>Blog</a><i>|</i><a>Services</a><i>|</i><a>Contact Us</a></nav>
<div class="copyright abs">© Copyright 2013 Meridian Commercial Realty. All Rights Reserved.</div>

</body>
</html>
```